Belle Lueur Hand Crafted Candles promotional flyer

Hand Crafted Soy Candles - I need a flyer to promote my candles and to give information on care of candles.I want this to use the design and colours I already have for my labels and the photo I have attached.I am aiming at a sophisticated market so would like to reflect this in the design.
Should appeal to sophisticated women who enjoy the pleasure of candles - to enhance their enjoyment of life - gives them the 'joie de vivre'.
the candles are hand crafted from all natural ingredients, environmentally friendly and with exquisite fragrances

Target Market(s)

sophisticated females

Industry/Entity Type

Promotional

Font styles to use
Script

Colors
cfeae6
ecdaeb

Requirements
Must have
• something expressing 'joie de vivre' - the enjoyment of candles
Should not have
• bright colours

```html
<!DOCTYPE html>
<html lang="en">
<head>
<meta charset="utf-8">
<title>Belle Lueur Hand Crafted Candles – Flyer</title>
<link rel="stylesheet" href="https://fonts.googleapis.com/css2?family=Great+Vibes&family=Raleway:wght@300;400;700&family=Roboto+Condensed:wght@300;400&family=Oswald:wght@400&family=Crimson+Text:wght@400;700&display=swap">
<style>
  :root {
    --stage: #e6e6e6;
    --paper: #ffffff;
    --mint: #cfeae6;
    --blush: #ecdaeb;
    --plum: #8b3a78;
    --teal: #1f7a74;
    --grey: #6b6c6f;
    --ink: #3e3f42;
    --bullet: #c79abb;
  }
  * { margin: 0; padding: 0; box-sizing: border-box; }
  html, body { width: 1200px; height: 1200px; overflow: hidden; }
  body { background: var(--stage); position: relative; }

  .flyer {
    position: absolute; left: 190px; top: 20px;
    width: 820px; height: 1160px;
    background: var(--paper); overflow: hidden;
  }
  .hero-art { position: absolute; right: 0; top: 0; width: 380px; height: 400px; }

  .kicker {
    position: absolute; left: 41px; top: 54px;
    font: 400 25px/1 "Oswald", sans-serif; color: var(--grey);
  }
  .brand-title {
    position: absolute; left: 62px; top: 98px; width: 320px;
    font: 400 98px/0.98 "Great Vibes", cursive; color: var(--plum);
  }
  .brand-title .line2 { display: block; padding-left: 34px; }
  .tagline {
    position: absolute; right: 451px; top: 300px; text-align: right;
    font: 300 23px/1.3 "Raleway", sans-serif; color: var(--grey);
  }
  .tagline strong { font-weight: 700; display: block; }

  .left-column { position: absolute; left: 41px; top: 370px; width: 360px; }
  .features {
    list-style: none; margin-left: 28px; margin-bottom: 36px;
    font: 400 21px/29px "Raleway", sans-serif; color: var(--teal);
  }
  .features li { white-space: nowrap; }
  .dot { display: inline-block; width: 8px; height: 8px; border-radius: 50%; background: var(--grey); opacity: .6; margin-right: 9px; vertical-align: middle; }
  .dot.pink { background: var(--bullet); opacity: 1; width: 6px; height: 6px; margin-right: 8px; }

  .section-title {
    font: 400 19px/1.2 "Raleway", sans-serif; color: var(--plum); margin-left: 21px; margin-bottom: 7px;
  }
  .section-title b { font-weight: 700; }

  .notes { list-style: none; font: 300 14.5px/20px "Roboto Condensed", sans-serif; color: var(--ink); }
  .notes li { padding-left: 18px; text-indent: -18px; margin-bottom: 4px; }

  .why-notes { margin-bottom: 30px; }
  .refill-notes { width: 240px; }

  .care-column { position: absolute; left: 423px; top: 405px; width: 372px; }
  .care-column .section-title { margin-left: 18px; margin-bottom: 8px; }
  .care-column .notes { font-size: 13.8px; line-height: 19.5px; }
  .care-column .notes li { margin-bottom: 3px; }
  .care-lower { margin-left: 125px; width: 240px; }

  .product-shot {
    position: absolute; left: 284px; top: 852px; width: 262px; height: 186px;
    background: linear-gradient(180deg, #dcdad6 0%, #f1eee8 45%, #c9c7c9 100%);
    border-radius: 6px;
  }

  .footer-band { position: absolute; left: 0; bottom: 0; width: 820px; height: 160px; }
  .phone {
    position: absolute; left: 68px; top: 1080px; display: flex; align-items: center; gap: 14px;
    font: 700 42px/1 "Crimson Text", serif; color: var(--teal);
  }
  .contact {
    position: absolute; right: 88px; top: 1075px; text-align: right;
    font: 400 21px/30px "Crimson Text", serif; letter-spacing: 1px; color: var(--ink);
  }
  .contact .web { color: var(--plum); font-weight: 700; letter-spacing: .3px; }
</style>
</head>
<body>
  <article class="flyer">
    <svg class="hero-art" viewBox="0 0 380 400">
      <defs>
        <linearGradient id="spaTones" x1="0" y1="0" x2="1" y2="1">
          <stop offset="0" stop-color="#f3d3d8"/>
          <stop offset="0.5" stop-color="#d8a89b"/>
          <stop offset="1" stop-color="#8a6a5a"/>
        </linearGradient>
      </defs>
      <ellipse cx="275" cy="80" rx="295" ry="310" fill="var(--mint)"/>
      <ellipse cx="290" cy="70" rx="275" ry="290" fill="url(#spaTones)" role="img" aria-label="Photo of a woman relaxing at a spa beside a lit pink pillar candle and orchids"/>
    </svg>

    <p class="kicker">THESE CANDLES WILL FILL YOU WITH</p>
    <h1 class="brand-title">Belle <span class="line2">Lueur</span></h1>
    <p class="tagline">AN EXUBERANT <strong>ENJOYMENT OF LIFE</strong></p>

    <section class="left-column">
      <ul class="features">
        <li><span class="dot"></span>Hand crafted soy candle creations</li>
        <li><span class="dot"></span>Completely non-toxic</li>
        <li><span class="dot"></span>Exquisite fragrances</li>
        <li><span class="dot"></span>Clean burning</li>
        <li><span class="dot"></span>Environmentally friendly</li>
      </ul>

      <h2 class="section-title">WHY <b>SOY</b> WAX?</h2>
      <ul class="notes why-notes">
        <li><span class="dot pink"></span>Soft smooth wax that burns clear – no soot or smoke</li>
        <li><span class="dot pink"></span>Soy wax candles burn up to 50% longer than traditional paraffin candles</li>
        <li><span class="dot pink"></span>Made form soya beans, a renewable natural resource that supports and sustains agriculture – it is biodegradable and environmentally friendly.</li>
        <li><span class="dot pink"></span>Soy wax burns cooler than paraffin and disperse the fragrance more fully.</li>
      </ul>

      <h2 class="section-title">CONTAINERS CAN BE<br><b>REFILLED</b></h2>
      <ul class="notes refill-notes">
        <li><span class="dot pink"></span>I offer a refill service – if you return your containers to me I can refill with the fragrance of your choice</li>
        <li><span class="dot pink"></span>Or if you have a special container you would like to use for your candle just contact me for a quote.</li>
        <li><span class="dot pink"></span>I have a wide range of fragrances – please contact me for details.</li>
      </ul>
    </section>

    <div class="product-shot" role="img" aria-label="Photo of four labelled soy candles in glass and blue containers"></div>

    <section class="care-column">
      <h2 class="section-title">HOW TO <b>CARE</b> FOR YOUR CANDLE</h2>
      <ul class="notes">
        <li><span class="dot pink"></span>When lighting you candle for the first time, allow the wax to melt all the way to the sides of the container – this creates a ‘memory’ and avoids ‘tunnelling’ as the candle burns.</li>
        <li><span class="dot pink"></span>Always trim the wick to about 6-8 mm before re-lighting your candle. This will ensure a long lasting candle, minimise soot and remove any mushrooming of the wick from a previous burn.</li>
        <li><span class="dot pink"></span>It is preferable to use a candle ‘snuffer’ to extinguish the flame, or a lid if the candle has one. Alternatively, you can dip the wick into the melted wax and then straightening. This wil stop the wick from smoking and help with relighting.</li>
        <li><span class="dot pink"></span>All Belle Lueur candles are hand poured not massed produced – although every effort is made to ensure consistency, every candle may be different.</li>
        <li><span class="dot pink"></span>Sometimes you may notice darker patches or wet spots – this is not a fault it is just the natural way the wax has set – it does not affect the candle in anyway.</li>
        <li><span class="dot pink"></span>The top of the candle may also appear slightly uneven – this is just a sign of natural soy wax being hand poured.</li>
      </ul>
      <ul class="notes care-lower">
        <li><span class="dot pink"></span>Do not leave your candle in the sunlight as it may turn a yellow colour – again this does not affect the candle in anyway – it just loses its creamy white colour.</li>
        <li><span class="dot pink"></span>As these candles contain no preservatives or chemicals it is recommended that they should be used within 6 months.</li>
      </ul>
    </section>

    <svg class="footer-band" viewBox="0 0 820 160" preserveAspectRatio="none">
      <path d="M0 10 C 180 50, 420 64, 820 48 L 820 160 L 0 160 Z" fill="var(--mint)"/>
    </svg>

    <div class="phone">
      <svg width="34" height="34" viewBox="0 0 34 34" aria-label="Phone">
        <circle cx="17" cy="17" r="15.5" fill="none" stroke="var(--plum)" stroke-width="1.6"/>
        <rect x="12" y="8" width="10" height="18" rx="2" fill="none" stroke="var(--plum)" stroke-width="1.6"/>
        <circle cx="17" cy="22.5" r="1.1" fill="var(--plum)"/>
      </svg>
      <span>021 555 0184</span>
    </div>
    <div class="contact">
      <div>claire.dunmore@mail.co.nz</div>
      <div class="web">www.mybellelueur.co.nz</div>
    </div>
  </article>
</body>
</html>
```